4 'Thank you' greetings cards designs

We are a small greetings card publisher and we need designs for a range of 'Thank you' greetings cards and notecards.
This project is for a total of 4 designs.
Please take a look at this board on Clipnest, to see the kind of thing we are looking for: https://www.pinboardly.example/marvk8150/gratitude-notes/
The cards will be printed at a maximum size of 131mm x 183mm (including a 3mm bleed) so please provide 300dpi CMYK files at this size. Please ensure that any text (or elements of the design that are not part of the bleed) are at least 11mm in from each edge. Also, please note that cards do not have to have a bleed if your design doesn't require it (e.g. a plain white background).
Please provide 2 designs in 'portrait' orientation and 2 in 'landscape'.
Please provide 2 designs that just have the words 'Thank you' and then 2 designs that include your choice of these alternative messages:
Thank you so much
Thanks very much
Thank you very much
Thanks a million
Just to say thank you
A big thank you
A really big thank you
Feel free to use an exclamation mark on a couple of your designs, if you wish!
Other than the above guidelines, everything else is up to you in terms of colours, fonts, shapes, etc. - but please use the Clipnest board to see the kind of designs we are looking for.
Thank you!

```html
<!DOCTYPE html>
<html lang="en">
<head>
<meta charset="utf-8">
<title>Thank You Card</title>
<link rel="stylesheet" href="https://fonts.googleapis.com/css2?family=Yellowtail&display=swap">
<style>
  :root {
    --card-bg: #f5e1fa;
    --frame: #6a0f4a;
    --ink: #6b0f4a;
    --ink-shadow: rgba(110, 95, 125, 0.5);
    --pink: #ff2fa8;
    --magenta: #ee10b8;
    --violet: #9a3bf2;
    --sky: #4fd0f5;
    --yellow: #f8f100;
    --red: #e80d0d;
    --navy: #2a12c4;
    --green: #33d56a;
    --orange: #ff8a10;
  }
  html, body {
    margin: 0;
    padding: 0;
    overflow: hidden;
  }
  .card {
    position: relative;
    width: 859px;
    height: 1200px;
    background: var(--card-bg);
    overflow: hidden;
  }
  .card-frame {
    position: absolute;
    left: 21px;
    top: 24px;
    width: 807px;
    height: 1180px;
    border: 6px solid var(--frame);
  }
  .puzzle-art {
    position: absolute;
    inset: 0;
    width: 859px;
    height: 1200px;
  }
  .greeting {
    position: absolute;
    inset: 0;
    margin: 0;
    font-family: "Yellowtail", cursive;
    font-weight: 400;
    color: var(--ink);
    text-shadow: 9px 8px 3px var(--ink-shadow);
  }
  .greeting-line {
    position: absolute;
    display: block;
    white-space: nowrap;
    line-height: 1;
  }
  .greeting-thank {
    left: 112px;
    top: 210px;
    font-size: 290px;
    letter-spacing: -6px;
  }
  .greeting-you {
    left: 190px;
    top: 540px;
    font-size: 300px;
    letter-spacing: -4px;
  }
</style>
</head>
<body>
  <main class="card">
    <div class="card-frame"></div>

    <h1 class="greeting">
      <span class="greeting-line greeting-thank">Thank</span>
      <span class="greeting-line greeting-you">You</span>
    </h1>

    <svg class="puzzle-art" viewBox="0 0 859 1200" xmlns="http://www.w3.org/2000/svg">
      <defs>
        <linearGradient id="corner-left-tones" x1="0" y1="0" x2="1" y2="0.4">
          <stop offset="0" stop-color="var(--magenta)"/>
          <stop offset="0.35" stop-color="var(--sky)"/>
          <stop offset="0.6" stop-color="var(--violet)"/>
          <stop offset="1" stop-color="var(--violet)"/>
        </linearGradient>
        <linearGradient id="corner-right-tones" x1="0" y1="0" x2="0.6" y2="1">
          <stop offset="0" stop-color="var(--red)"/>
          <stop offset="0.35" stop-color="var(--yellow)"/>
          <stop offset="0.7" stop-color="var(--pink)"/>
          <stop offset="1" stop-color="var(--pink)"/>
        </linearGradient>
        <linearGradient id="base-tones" x1="0" y1="0" x2="1" y2="0.3">
          <stop offset="0" stop-color="var(--yellow)"/>
          <stop offset="0.15" stop-color="var(--red)"/>
          <stop offset="0.32" stop-color="var(--magenta)"/>
          <stop offset="0.5" stop-color="var(--green)"/>
          <stop offset="0.65" stop-color="var(--navy)"/>
          <stop offset="0.8" stop-color="var(--orange)"/>
          <stop offset="1" stop-color="var(--pink)"/>
        </linearGradient>
      </defs>

      <g role="img" aria-label="Cluster of colourful jigsaw puzzle pieces in the top left corner">
        <polygon fill="url(#corner-left-tones)"
          points="0,0 450,0 440,38 270,45 262,108 170,118 160,165 0,172"/>
      </g>

      <g role="img" aria-label="Cluster of red, yellow and pink jigsaw puzzle pieces in the top right corner">
        <polygon fill="url(#corner-right-tones)"
          points="652,0 859,0 859,200 792,225 702,200 706,120 652,60"/>
      </g>

      <g role="img" aria-label="Band of overlapping multicoloured jigsaw puzzle pieces along the bottom of the card">
        <polygon fill="url(#base-tones)"
          points="0,822 60,812 142,830 152,960 250,1000 330,1000 400,962 440,912 560,902 610,832 700,802 722,742 840,736 859,752 859,1200 0,1200"/>
      </g>
    </svg>
  </main>
</body>
</html>
```